Dietitian needs a new business card design

I need a new business card design for my nutrition business that provides individual clinical nutrition advice for people with medical conditions. Business cards will be handed out to doctors, specialists and clients so will need to be sharp and project an image of professionalism

Target Market(s)

My clients are typically referred by doctors or specialists and the card will be used to handout to clients and their doctors.

Industry/Entity Type

Medical

Contact Information for Business Card

The business card will require the details below. These details can be found from my website https://www.kelvarrowclinic.com.au/

Font styles to use
Serif

Colors

Designer to choose colors to be used in the design.

Requirements
Must have
• 1. It needs be professional and contemporary
• 2. It needs to incorporate my logo
• 3. It needs space to write appointment times and dates
• 4. It needs to provide my phone number, fax number, email address and my web address
Nice to have
• Include the Registered Tovance Clinician Logo
• I have access to Framellow if required
• The locations I practise from
Should not have
• Pictures of food
• Spelling MIstakes

```html
<!DOCTYPE html>
<html lang="en">
<head>
<meta charset="utf-8">
<title>Kelvarrow Clinic – Business Card</title>
<link href="https://fonts.googleapis.com/css2?family=Cinzel:wght@400;500&family=Source+Sans+3:ital,wght@0,400;1,400&display=swap" rel="stylesheet">
<style>
  :root {
    --backdrop: #1b1b1b;
    --card-white: #f3f3f3;
    --paper: #ffffff;
    --navy: #1d3f9c;
    --blue: #1a5fb4;
    --blue-deep: #123c9c;
    --green: #7ab928;
    --ink: #3a3a3a;
    --label-grey: #8a8a8a;
    --rule: #a9bfdc;
    --badge: #f07b23;
  }
  * { margin: 0; padding: 0; box-sizing: border-box; }
  html, body { width: 1200px; height: 900px; overflow: hidden; background: var(--backdrop); }
  .canvas { position: relative; width: 1200px; height: 900px; }

  .card { position: absolute; top: 200px; width: 310px; height: 502px; overflow: hidden;
          box-shadow: 3px 4px 8px rgba(0,0,0,.55); }

  /* Front */
  .card-front { left: 253px; background: var(--card-white); border-radius: 56px 0 56px 0; }
  .brand { position: absolute; left: 38px; top: 140px; display: flex; align-items: center; gap: 10px; }
  .brand-dot { width: 34px; height: 34px; border-radius: 50%; background: var(--blue); }
  .brand-name { font-family: "Cinzel", serif; font-size: 25px; color: var(--navy); }
  .holder { position: absolute; left: 32px; top: 326px; }
  .holder-name { font-family: "Cinzel", serif; font-size: 19px; color: var(--navy); letter-spacing: .5px; }
  .holder-role { font-family: "Source Sans 3", sans-serif; font-size: 14px; color: var(--ink); margin-top: 1px; }
  .contacts { position: absolute; left: 32px; top: 389px; list-style: none;
              font-family: "Source Sans 3", sans-serif; font-size: 13.5px; color: var(--ink); }
  .contacts li { display: flex; align-items: center; gap: 4px; height: 18px; }
  .contacts svg { width: 12px; height: 12px; fill: var(--navy); }

  /* Back */
  .card-back { left: 627px; background: var(--paper); border-radius: 0 50px 0 50px; }
  .band-top { position: absolute; left: 0; top: 0; width: 100%; height: 145px;
              background: linear-gradient(135deg, var(--blue) 0%, var(--blue-deep) 100%); }
  .band-bottom { position: absolute; left: 0; bottom: 0; width: 100%; height: 89px;
                 background: linear-gradient(135deg, var(--blue-deep) 0%, var(--blue) 100%); }
  .seal { position: absolute; left: 51px; top: 0; width: 200px; height: 200px; border-radius: 50%;
          background: var(--paper); display: flex; align-items: center; justify-content: center; top: 1px; }
  .seal-name { font-family: "Cinzel", serif; font-size: 24px; color: var(--navy); }
  .appointment-title { position: absolute; left: 0; width: 100%; top: 210px; text-align: center;
                       font-family: "Cinzel", serif; font-size: 19px; color: var(--navy); letter-spacing: .3px; }
  .field { position: absolute; left: 38px; width: 250px; border-bottom: 1.5px solid var(--rule);
           font-family: "Cinzel", serif; font-size: 17px; color: var(--label-grey); padding-left: 2px; padding-bottom: 2px; }
  .field-date { top: 255px; }
  .field-time { top: 306px; }
  .notice { position: absolute; left: 0; width: 100%; top: 356px; text-align: center;
            font-family: "Source Sans 3", sans-serif; font-style: italic; font-size: 14px; line-height: 18px; color: #222; }
  .badge-holder { position: absolute; left: 79px; top: 413px; width: 152px; height: 73px;
                  background: var(--paper); border-radius: 0 0 3px 3px; }
  .badge { position: absolute; left: 15px; top: 5px; width: 120px; height: 56px; background: var(--badge); }
</style>
</head>
<body>
<div class="canvas">

  <section class="card card-front">
    <div class="brand">
      <span class="brand-dot"></span>
      <span class="brand-name">Kelvarrow</span>
    </div>
    <div class="holder">
      <h1 class="holder-name">MARTIN ELLSWORTH</h1>
      <p class="holder-role">Registered Tovance Clinician</p>
    </div>
    <ul class="contacts">
      <li><svg viewBox="0 0 12 12"><path d="M1 4c0-2 2-3 5-3s5 1 5 3l-2 1-1-1.5H4L3 5zM2 6h8l1 5H1z"/></svg>0400 555 128</li>
      <li><svg viewBox="0 0 12 12"><path d="M3 1h6v3H3zM1 5h10v5H9V8H3v2H1zM3 9h6v2H3z"/></svg>+613 6300 4417</li>
      <li><svg viewBox="0 0 12 12"><path d="M1 3h10v6H1zM1 3l5 4 5-4" stroke="#fff" stroke-width=".8"/></svg>martin@kelvarrowclinic.com.au</li>
      <li><svg viewBox="0 0 12 12"><circle cx="6" cy="6" r="5"/></svg>www.kelvarrowclinic.com.au</li>
    </ul>
  </section>

  <section class="card card-back">
    <div class="band-top"></div>
    <div class="band-bottom"></div>
    <div class="seal"><span class="seal-name">Kelvarrow</span></div>
    <h2 class="appointment-title">YOUR NEXT APPOINTMENT</h2>
    <div class="field field-date">DATE</div>
    <div class="field field-time">TIME</div>
    <p class="notice">If unable to keep the appointment,<br>please give 24 hoursnotice</p>
    <div class="badge-holder"><div class="badge"></div></div>
  </section>

</div>
</body>
</html>
```